New Flyer Design Project

We need a flyer for our upcoming Rising Builders Forum.

5th Annual Rising Builders Forum
by the Council for Stewardship of Built Ventures (C-SBuV)
Theme: Step Forward
Date: January 24, 2020
Location: Bluestone Lodge Hotel and Conference Center, San Marcos, TX
#StepForward

This is event is put together by C-SBuV's Rising Builders Ring of Merit. I have a logo for the Ring of Merit, but not something that indicates it's the Rising Builders Ring.

More about the Forum (please don't include on the flyer): This Forum provides a venue to openly discuss issues affecting women in our industry and ideas and strategies to address those issues.

Architecture, Construction and Engineering are all struggling with a tremendous shortage of skilled talent. It is more important than ever for organizations to be able to attract, support and retain a talented workforce and to encourage more women to pursue and build vibrant careers in architecture, engineering and construction. Unfortunately, their attrition rate also remains high in these industries. Developing and retaining a skilled workforce includes identifying and addressing the specific needs of women in our industry. Man or Woman; Male or Female Brain, C-SBuV’s Rising Builders Forum will give you and your team the tools you need to excel as an Employer of Choice and a roadmap for individual continued career planning and success .

This unique Forum provides a venue to engage everyone from executives to those just beginning their careers with active, hands-on sessions and vibrant networking with the best and brightest in the A/E/C industry. In our usual C-SBuV Forum style, Keynotes become table participants and table participants become presenters, encouraging participants to assimilate what they are learning. Join local, state and national leaders and subject matter experts as we candidly explore and address the issues affecting women in our industry .

```html
<!DOCTYPE html>
<html lang="en">
<head>
<meta charset="utf-8">
<title>5th Annual Rising Builders Forum</title>
<link rel="stylesheet" href="https://fonts.googleapis.com/css2?family=League+Gothic&family=Oswald:wght@500;600&family=Open+Sans:wght@400;700&display=swap">
<style>
  :root {
    --purple: #5f2a8c;
    --purple-deep: #3b2a78;
    --pink: #ec0f7a;
    --yellow: #f4e22c;
    --gold: #f8b928;
    --orange: #f39228;
    --orange-red: #ee5f2c;
    --white: #ffffff;
  }
  * { margin: 0; padding: 0; box-sizing: border-box; }
  html, body { width: 848px; height: 1200px; overflow: hidden; }
  body { background: var(--gold); }
  .flyer {
    position: relative;
    width: 848px; height: 1200px; overflow: hidden;
    background: radial-gradient(circle at 100% 0%, var(--yellow) 0%, var(--gold) 45%, var(--orange) 85%);
  }
  .backdrop { position: absolute; inset: 0; }
  .title {
    position: absolute; left: 120px; top: 62px;
    font-family: "League Gothic", "Oswald", sans-serif; font-weight: 400;
    transform: rotate(-4deg); transform-origin: left top;
    white-space: nowrap;
  }
  .title__edition {
    display: flex; align-items: flex-start;
    color: var(--purple); font-size: 196px; line-height: .8;
  }
  .title__edition sup { font-size: 84px; line-height: .8; margin: 6px 28px 0 6px; }
  .title__name {
    display: block; color: var(--pink);
    font-size: 96px; line-height: .85; margin-top: 4px;
  }
  .group-art {
    position: absolute; left: 114px; top: 430px; width: 612px; height: 560px;
    border-radius: 48% 48% 0 0;
    background: linear-gradient(180deg, #f3c3cf 0%, #d86a82 55%, #6a3440 100%);
    opacity: .9;
  }
  .hashtag {
    position: absolute; left: 52px; top: 976px;
    font-family: "League Gothic", sans-serif; font-size: 96px; line-height: .85;
    color: var(--pink); white-space: nowrap;
    transform: rotate(-7deg); transform-origin: left top;
  }
  .details {
    position: absolute; left: 96px; top: 1066px;
    font-family: "Oswald", sans-serif; font-style: italic; font-weight: 500;
    color: var(--purple); transform: rotate(-5deg); transform-origin: left top;
  }
  .details__venue { display: flex; align-items: center; gap: 10px; font-size: 24px; line-height: 1.2; white-space: nowrap; }
  .details__date {
    position: absolute; left: 104px; top: 1146px;
    display: flex; align-items: center; gap: 12px;
    font-family: "Oswald", sans-serif; font-style: italic; font-weight: 500;
    font-size: 24px; color: var(--purple); transform: rotate(-4deg);
  }
  .presenters {
    position: absolute; left: 546px; top: 1040px; width: 200px;
    display: flex; flex-direction: column; align-items: center; gap: 34px;
    font-family: "Open Sans", sans-serif; color: var(--white);
  }
  .org { text-align: center; }
  .org__name { display: flex; align-items: center; justify-content: center; gap: 8px; font-size: 21px; font-weight: 400; line-height: 1.1; }
  .org__mark { width: 22px; height: 22px; border-radius: 50%; background: var(--white); flex: none; }
  .org__tagline { font-size: 7px; font-weight: 700; margin-top: 3px; white-space: nowrap; }
  .divider { position: absolute; left: 757px; top: 1018px; width: 2px; height: 168px; background: var(--white); }
  .presented-by {
    position: absolute; left: 776px; top: 1026px;
    writing-mode: vertical-rl;
    font-family: "Oswald", sans-serif; font-weight: 600; font-size: 19px;
    letter-spacing: 1px; color: var(--white);
  }
</style>
</head>
<body>
<main class="flyer">
  <svg class="backdrop" width="848" height="1200" viewBox="0 0 848 1200" aria-hidden="true">
    <defs>
      <linearGradient id="lower-band" x1="0" y1="0" x2="1" y2="0">
        <stop offset="0" stop-color="#f1e22e"/>
        <stop offset="0.55" stop-color="#f6a52a"/>
        <stop offset="1" stop-color="#ee5f2c"/>
      </linearGradient>
      <linearGradient id="swoosh" x1="0" y1="0" x2="1" y2="0">
        <stop offset="0" stop-color="#6a2e92"/>
        <stop offset="1" stop-color="#2f2870"/>
      </linearGradient>
    </defs>
    <circle class="spotlight" cx="435" cy="690" r="369" fill="var(--pink)"/>
    <g class="orbit" fill="none" stroke="var(--purple)" stroke-width="3" stroke-linecap="round">
      <path d="M299 318 A398 398 0 0 1 571 318"/>
      <path d="M190 366 A398 398 0 0 1 252 334"/>
      <path d="M648 352 A398 398 0 0 1 768 474"/>
      <path d="M160 395 A405 405 0 0 0 40 650"/>
      <path d="M40 790 A405 405 0 0 0 80 900"/>
      <path d="M832 620 A405 405 0 0 1 800 960"/>
    </g>
  </svg>

  <div class="group-art" role="img" aria-label="Illustration of a diverse group of nine women standing together"></div>

  <svg class="backdrop" width="848" height="1200" viewBox="0 0 848 1200" aria-hidden="true">
    <path d="M0 792 Q480 1090 848 906 L848 1200 L0 1200 Z" fill="url(#lower-band)"/>
    <path d="M0 792 Q480 1090 848 906 L848 926 Q480 1112 0 815 Z" fill="url(#swoosh)"/>
    <line x1="4" y1="1150" x2="486" y2="1096" stroke="var(--orange-red)" stroke-width="3" stroke-dasharray="10 7"/>
  </svg>

  <h1 class="title">
    <span class="title__edition">5<sup>TH</sup>ANNUAL</span>
    <span class="title__name">RISING BUILDERS FORUM</span>
  </h1>

  <p class="hashtag">#STEPFORWARD</p>

  <div class="details">
    <p class="details__venue">
      <svg width="28" height="40" viewBox="0 0 30 42" aria-hidden="true"><path d="M15 0C7 0 0 6.5 0 15c0 10 15 27 15 27s15-17 15-27C30 6.5 23 0 15 0zm0 21a6 6 0 1 1 0-12 6 6 0 0 1 0 12z" fill="var(--purple)"/></svg>
      <span>Bluestone Lodge Hotel and<br>Conference Center, San Marcos, TX</span>
    </p>
  </div>

  <p class="details__date">
    <svg width="30" height="30" viewBox="0 0 30 30" aria-hidden="true"><g fill="var(--purple)"><rect x="1" y="5" width="28" height="24" rx="3" fill="none" stroke="var(--purple)" stroke-width="3"/><rect x="1" y="5" width="28" height="7"/><rect x="7" y="1" width="3" height="7"/><rect x="20" y="1" width="3" height="7"/><rect x="7" y="15" width="4" height="3"/><rect x="13" y="15" width="4" height="3"/><rect x="19" y="15" width="4" height="3"/><rect x="7" y="21" width="4" height="3"/><rect x="13" y="21" width="4" height="3"/><rect x="19" y="21" width="4" height="3"/></g></svg>
    <span>January 24, 2020</span>
  </p>

  <div class="presenters">
    <div class="org">
      <p class="org__name"><span class="org__mark"></span>Ring of Merit</p>
      <p class="org__tagline">Council for Stewardship of Built Ventures</p>
    </div>
    <div class="org">
      <p class="org__name"><span class="org__mark"></span>C-SBuV</p>
      <p class="org__tagline">Council for Stewardship of Built Ventures</p>
    </div>
  </div>
  <div class="divider"></div>
  <p class="presented-by">PRESENTED BY</p>
</main>
</body>
</html>
```